Outdoor sign for Brindle Auto Restoration

I need a horizontal 4'x 8' outdoor roadside sign for my classic auto restoration business. I have uploaded colors and our logo. Needs the Brindle name, a prominent Classic AUTO RESTORATION, phone number and website. We rebuild and restore vintage cars, trucks and 4x4s. I'd like something clean but possibly retro. Classic Auto Restoration is more important than the Brindle name. It needs to be visible and readable from the street. NO CLIP ART

Target Market(s)

Customers who need their vintage care restored or upgraded. Men and women ages 25-75

Industry/Entity Type

Automotive

Colors
FFC000
F8CF3A
FAE287
FDF2CF
FEFAEE

Requirements
Must have
• Legible. Bright. Readable as a backlit 4' x 8' large horizontal sign (roughly 120cm X 240cm)
Nice to have
• Use of the Brindle logo/type, Complete or Classic before prominent AUTO RESTORATION
Should not have
• Clip art of old cars or icons. And we don't want the Brindle Logo from the website because it wont be legible from the road. I have included the Illustrator file for Brindle text in the uploads

```html
<!DOCTYPE html>
<html lang="en">
<head>
<meta charset="utf-8">
<title>Brindle Complete Auto Restoration – Roadside Sign</title>
<link rel="stylesheet" href="https://fonts.googleapis.com/css2?family=Oswald:wght@600;700&family=Yellowtail&family=Roboto+Condensed:wght@700&display=swap">
<style>
  :root {
    --ink: #231f20;
    --amber: #f7ad1e;
    --paper: #ffffff;
    --backdrop: #ffffff;
  }
  html, body {
    margin: 0;
    padding: 0;
    width: 1036px;
    height: 1200px;
    overflow: hidden;
    background: var(--backdrop);
  }
  .canvas {
    position: relative;
    width: 1036px;
    height: 1200px;
    display: flex;
    align-items: center;
    justify-content: center;
  }
  .sign {
    width: 960px;
    height: 483px;
    display: block;
  }
  .brand-name { font-family: "Oswald", sans-serif; font-weight: 700; fill: var(--amber); }
  .tagline-script { font-family: "Yellowtail", cursive; fill: var(--ink); }
  .headline { font-family: "Oswald", sans-serif; font-weight: 700; }
  .headline-shadow { fill: var(--ink); }
  .headline-face { fill: var(--paper); }
  .phone { font-family: "Roboto Condensed", sans-serif; font-weight: 700; fill: var(--paper); }
  .website { font-family: "Roboto Condensed", sans-serif; font-weight: 700; fill: var(--amber); }
</style>
</head>
<body>
<main class="canvas">
  <svg class="sign" viewBox="0 0 1090 548" xmlns="http://www.w3.org/2000/svg" aria-label="Brindle Complete Auto Restoration sign">
    <!-- base panel -->
    <rect class="panel" x="0" y="0" width="1090" height="548" fill="var(--paper)"/>
    <!-- dark upper field -->
    <polygon class="dark-field" points="0,0 1090,0 1090,155 0,307" fill="var(--ink)"/>
    <!-- amber sweep band -->
    <polygon class="amber-band" points="0,307 1090,155 1090,215 0,362" fill="var(--amber)"/>

    <!-- tool artwork placeholders -->
    <g role="img" aria-label="White wrench illustration, left">
      <rect x="-20" y="120" width="300" height="34" rx="17" fill="var(--paper)" transform="rotate(-30 130 137)"/>
    </g>
    <g role="img" aria-label="White wrench illustration, right">
      <rect x="820" y="70" width="230" height="34" rx="17" fill="var(--paper)" transform="rotate(28 935 87)"/>
    </g>

    <!-- business name -->
    <text class="brand-name" x="540" y="90" font-size="64" text-anchor="middle" letter-spacing="1">BRINDLE</text>

    <!-- central oval -->
    <ellipse class="oval" cx="540" cy="259" rx="455" ry="118" fill="var(--amber)" stroke="var(--paper)" stroke-width="6"/>

    <text class="tagline-script" x="535" y="212" font-size="72" text-anchor="middle">Complete</text>

    <g class="headline" font-size="88">
      <text class="headline-shadow" x="548" y="306" text-anchor="middle" textLength="745" lengthAdjust="spacingAndGlyphs">AUTO RESTORATION</text>
      <text class="headline-face" x="543" y="300" text-anchor="middle" textLength="745" lengthAdjust="spacingAndGlyphs">AUTO RESTORATION</text>
    </g>

    <!-- phone ribbon -->
    <path class="ribbon" d="M275,337 Q548,352 822,337 L790,390 L822,437 Q548,452 275,437 L307,390 Z" fill="var(--ink)" stroke="var(--paper)" stroke-width="4"/>
    <circle cx="330" cy="394" r="5" fill="var(--paper)"/>
    <circle cx="768" cy="394" r="5" fill="var(--paper)"/>
    <text class="phone" x="549" y="422" font-size="72" text-anchor="middle" textLength="400" lengthAdjust="spacingAndGlyphs">501-555-0142</text>

    <!-- website rule -->
    <line x1="28" y1="503" x2="365" y2="503" stroke="var(--ink)" stroke-width="3"/>
    <line x1="725" y1="503" x2="1065" y2="503" stroke="var(--ink)" stroke-width="3"/>
    <text class="website" x="545" y="510" font-size="22" text-anchor="middle">www.brindleautoworks.com</text>

    <!-- frame -->
    <rect class="frame" x="1.5" y="1.5" width="1087" height="545" fill="none" stroke="var(--ink)" stroke-width="3"/>
  </svg>
</main>
</body>
</html>
```